Bramwell Resources Ltd. - Refreshed business card challenge

A revised, refreshed business card design for my oil and gas company using my existing logo. Feel free to be as creative as you like!

Target Market(s)

bankers, lawyers

Industry/Entity Type

Oil And Gas Exploration

Contact Information for Business Card

See the "Must Haves" section

Font styles to use
Serif
Sans Serif

Colors

Designer to choose colors to be used in the design.

Requirements
Must have
• Existing business logo, name, title, email, phone number, business address
• Neil Hadley, CA, CPA
• Vice President Finance & Chief Financial Officer
• nhadley@bramwellresources-mail.com
• office: (587)555-0142
• cell: (403)555-0187
• 1400, 815 4 Street S.W.
• Calgary, AB
• T2P 4K8
Should not have
• Should not be plain and boring.

```html
<!DOCTYPE html>
<html lang="en">
<head>
<meta charset="utf-8">
<title>Bramwell Resources Ltd. – Business Card</title>
<link rel="stylesheet" href="https://fonts.googleapis.com/css2?family=Nunito+Sans:ital,wght@0,400;0,600;0,700;0,800;1,600&display=swap">
<style>
  :root {
    --forest: #004a30;
    --bark: #4f2812;
    --paper: #ffffff;
    --backdrop: #e4e1db;
  }
  * { box-sizing: border-box; margin: 0; padding: 0; }
  html, body { width: 1154px; height: 1200px; overflow: hidden; }
  body {
    background: var(--backdrop);
    font-family: "Nunito Sans", sans-serif;
    color: var(--forest);
    position: relative;
  }
  .card {
    position: absolute;
    left: 77px;
    width: 1000px;
    height: 560px;
    background: var(--paper);
    box-shadow: 0 4px 14px rgba(0,0,0,.18);
    overflow: hidden;
  }
  .card--front { top: 30px; }
  .card--back { top: 610px; }
  .card__bands { position: absolute; top: 0; left: 0; width: 1000px; height: 120px; }

  .wordmark {
    font-weight: 800;
    color: var(--forest);
    letter-spacing: -0.5px;
    line-height: 1;
  }
  .card--front .wordmark {
    position: absolute;
    top: 215px;
    left: 0; right: 0;
    text-align: center;
    font-size: 78px;
  }
  .card--front .wordmark span { display: block; font-size: 30px; letter-spacing: 6px; margin-top: 10px; }

  .address {
    position: absolute;
    bottom: 48px;
    left: 0; right: 0;
    text-align: center;
    font-weight: 800;
    font-size: 27px;
    letter-spacing: .5px;
  }
  .address .dot { margin: 0 10px; }

  .card--back .wordmark {
    position: absolute;
    left: 60px;
    top: 285px;
    width: 420px;
    font-size: 54px;
  }
  .card--back .wordmark span { display: block; font-size: 21px; letter-spacing: 4px; margin-top: 8px; }
  .divider {
    position: absolute;
    left: 500px;
    top: 185px;
    width: 3px;
    height: 270px;
    background: var(--bark);
  }
  .contact { position: absolute; left: 545px; top: 200px; }
  .contact__name { font-size: 34px; font-weight: 700; letter-spacing: .3px; }
  .contact__name small { font-size: 22px; font-weight: 600; }
  .contact__title { font-style: italic; font-weight: 600; font-size: 21px; line-height: 28px; margin-top: 6px; }
  .contact__phones { margin-top: 16px; font-size: 21px; font-weight: 600; line-height: 34px; }
  .contact__phones b { display: inline-block; width: 30px; font-weight: 600; }
  .contact__web { margin-top: 14px; font-size: 20px; font-weight: 600; line-height: 38px; }
</style>
</head>
<body>

<section class="card card--front" aria-label="Card front">
  <svg class="card__bands" viewBox="0 0 1000 120" aria-hidden="true">
    <polygon points="0,60 700,60 0,100" fill="var(--bark)"/>
    <rect x="0" y="0" width="1000" height="62" fill="var(--forest)"/>
  </svg>
  <div class="wordmark">Bramwell<span>RESOURCES</span></div>
  <p class="address">1400, 815 4 STREET<span class="dot">·</span>S.W. CALGARY<span class="dot">·</span>ALBERTA<span class="dot">·</span>T2P 4K8</p>
</section>

<section class="card card--back" aria-label="Card back">
  <svg class="card__bands" viewBox="0 0 1000 120" aria-hidden="true">
    <polygon points="300,70 1000,70 1000,118" fill="var(--bark)"/>
    <rect x="0" y="0" width="1000" height="72" fill="var(--forest)"/>
  </svg>
  <div class="wordmark">Bramwell<span>RESOURCES</span></div>
  <div class="divider"></div>
  <div class="contact">
    <h1 class="contact__name">NEIL HADLEY<small>, CA, CPA</small></h1>
    <p class="contact__title">Vice President Finance<br>Chief Financial Officer</p>
    <p class="contact__phones"><b>t.</b>(587) 555-0142<br><b>m.</b>(403) 555-0187</p>
    <p class="contact__web">nhadley@bramwellresources-mail.com<br>www.bramwellresources-mail.com</p>
  </div>
</section>

</body>
</html>
```